TernQuay Business Cards

Create business cards for our exciting new software company. We provide cloud billing systems and provisioning software for campany that need monthly SaaS and Cloud Billing

Target Market(s)

Enterprise businesses, b2b, telecom carriers, software manufactures

Industry/Entity Type

Software

```html
<!DOCTYPE html>
<html lang="en">
<head>
<meta charset="utf-8">
<title>TernQuay Business Cards</title>
<link rel="stylesheet" href="https://fonts.googleapis.com/css2?family=Montserrat:wght@400;500&family=Open+Sans:wght@400&display=swap">
<style>
  :root {
    --backdrop: #2f2f31;
    --navy: #1f3450;
    --navy-deep: #1b2e48;
    --sky: #7cc6ec;
    --steel: #3f7aa5;
    --paper: #ffffff;
    --mist: #6f8193;
  }
  * { margin: 0; padding: 0; box-sizing: border-box; }
  html, body { width: 1200px; height: 900px; overflow: hidden; }
  body { background: var(--backdrop); position: relative; font-family: "Montserrat", sans-serif; }

  .card { position: absolute; top: 308px; width: 514px; height: 284px; overflow: hidden; }
  .card-front { left: 73px; background: linear-gradient(180deg, var(--navy) 0%, var(--navy) 60%, var(--navy-deep) 100%); }
  .card-back { left: 615px; background: var(--navy); }

  .brand-dot { position: absolute; border-radius: 50%; }
  .wordmark { position: absolute; font-family: "Montserrat", sans-serif; font-weight: 500; letter-spacing: 0.5px; line-height: 1; white-space: nowrap; }
  .tagline { position: absolute; text-align: right; text-transform: uppercase; font-weight: 400; line-height: 1.5; white-space: nowrap; }

  .card-front .brand-dot { left: 104px; top: 122px; width: 62px; height: 62px; background: var(--sky); }
  .card-front .wordmark { left: 184px; top: 144px; font-size: 46px; color: var(--sky); }
  .card-front .tagline { right: 100px; top: 200px; font-size: 8.5px; color: var(--paper); letter-spacing: 1.6px; }

  .back-panel-light { position: absolute; left: 0; top: 0; width: 257px; height: 100%; background: var(--paper); }
  .card-back .brand-dot { left: 28px; top: 144px; width: 34px; height: 34px; background: var(--steel); }
  .card-back .wordmark { left: 72px; top: 148px; font-size: 27px; color: var(--steel); }
  .card-back .tagline { right: 290px; top: 182px; font-size: 5.5px; color: var(--mist); letter-spacing: 1.2px; }

  .holder { position: absolute; right: 26px; top: 56px; text-align: right; }
  .holder-name { font-size: 19px; font-weight: 400; color: var(--sky); letter-spacing: 2.5px; line-height: 1.2; font-variant: small-caps; text-transform: lowercase; }
  .holder-name span { display: block; }
  .holder-role { margin-top: 6px; font-size: 12px; color: var(--paper); letter-spacing: 1.8px; text-transform: uppercase; }

  .contact { position: absolute; right: 26px; top: 137px; list-style: none; font-family: "Open Sans", sans-serif; font-size: 12px; color: var(--paper); text-align: right; }
  .contact li { display: flex; justify-content: flex-end; align-items: center; gap: 6px; height: 15.5px; }
  .contact li.gap { margin-top: 8px; }
  .contact svg { width: 11px; height: 11px; fill: var(--sky); flex: none; }
  .contact .spacer { width: 11px; flex: none; }
</style>
</head>
<body>
  <section class="card card-front" aria-label="Card front">
    <span class="brand-dot" aria-hidden="true"></span>
    <div class="wordmark">TernQuay</div>
    <p class="tagline">Cloud billing and<br>operational support systems</p>
  </section>

  <section class="card card-back" aria-label="Card back">
    <div class="back-panel-light"></div>
    <span class="brand-dot" aria-hidden="true"></span>
    <div class="wordmark">TernQuay</div>
    <p class="tagline">Cloud billing and<br>operational support systems</p>

    <div class="holder">
      <p class="holder-name"><span>Marcus</span><span>Ellery</span></p>
      <p class="holder-role">Managing Director</p>
    </div>

    <ul class="contact">
      <li>48 Harbor Lane
        <svg viewBox="0 0 12 12"><path d="M6 0.5a4 4 0 0 0-4 4c0 3 4 7 4 7s4-4 4-7a4 4 0 0 0-4-4zm0 5.6a1.6 1.6 0 1 1 0-3.2 1.6 1.6 0 0 1 0 3.2z"/></svg>
      </li>
      <li>Millbrook, New York 12545<span class="spacer"></span></li>
      <li>555 201 44 18
        <svg viewBox="0 0 12 12"><path d="M3.5 0.5h5a1 1 0 0 1 1 1v9a1 1 0 0 1-1 1h-5a1 1 0 0 1-1-1v-9a1 1 0 0 1 1-1zm0.6 1.4v7h3.8v-7zm1.9 7.7a.6.6 0 1 0 0 1.2.6.6 0 0 0 0-1.2z"/></svg>
      </li>
      <li>555 201 44 19
        <svg viewBox="0 0 12 12"><path d="M3 0.5h6v3H3zM1.5 4h9a1 1 0 0 1 1 1v4h-2v2.5h-7V9h-2V5a1 1 0 0 1 1-1zm2 4v2.5h5V8z"/></svg>
      </li>
      <li class="gap">info@ternquay.com
        <svg viewBox="0 0 12 12"><path d="M0.5 2.5h11v7h-11zM1.2 3l4.8 3.6L10.8 3z" fill-rule="evenodd"/></svg>
      </li>
      <li>www.ternquay.com
        <svg viewBox="0 0 12 12"><path d="M6 0.5a5.5 5.5 0 1 0 0 11 5.5 5.5 0 0 0 0-11zm0 1c.7 0 1.5 1.5 1.7 3.8H4.3C4.5 3 5.3 1.5 6 1.5zM1.5 6.7h1.9c.1 1.4.3 2.5.7 3.2a4.5 4.5 0 0 1-2.6-3.2zm0-1.4A4.5 4.5 0 0 1 4.1 2.1c-.4.8-.6 1.9-.7 3.2zm4.5 5.2c-.7 0-1.5-1.5-1.7-3.8h3.4C7.5 9 6.7 10.5 6 10.5zm1.9-.6c.4-.7.6-1.8.7-3.2h1.9a4.5 4.5 0 0 1-2.6 3.2zm.7-4.6c-.1-1.3-.3-2.4-.7-3.2a4.5 4.5 0 0 1 2.6 3.2z"/></svg>
      </li>
    </ul>
  </section>
</body>
</html>
```